Business Card for a Child Psychologist

I am a psychologist working with children and families and need a business card to give to clients and referral sources. I see children of all ages, so it should not look too young - as it will be for older children too. My work involves dealing with families in difficult situations, likes divorce, or with issues such as depression and anxiety. The design should communicate that I provide an open,warm, friendly, and caring atmosphere. I want to convey a sense of hope and positivity. Using colors like blues, purples

Target Market(s)

Families, doctors, family law attorneys

Industry/Entity Type

Psychology

Contact Information for Business Card

Lorna Pettigrew, Ph.D.
462 W. Brambleton, Suite 2150
Chicago, Illinois 60688
312-555-0173
drlornampettigrew@quenmail.example

Font styles to use
Script

Requirements
Must have
• A Logo to go with the details of my contact information.
Should not have
• Nothing in the shape of a brain. Nothing sad, or that looks too clinical.

```html
<!DOCTYPE html>
<html lang="en">
<head>
<meta charset="utf-8">
<title>Lorna Pettigrew, Ph.D. — Business Card</title>
<link href="https://fonts.googleapis.com/css2?family=Sacramento&family=EB+Garamond:wght@400;500&display=swap" rel="stylesheet">
<style>
  :root {
    --backdrop: #3a3c45;
    --card-blue: #adc5ce;
    --band-pale: #dde8ec;
    --mark-white: #f7fafb;
    --ink: #4f6f79;
    --paper: #ffffff;
  }
  * { margin: 0; padding: 0; box-sizing: border-box; }
  html, body { width: 1200px; height: 1200px; overflow: hidden; }
  body { background: var(--backdrop); position: relative; font-family: "EB Garamond", Georgia, serif; }

  .card {
    position: absolute;
    left: 317px;
    width: 589px;
    height: 382px;
    border-radius: 36px;
    overflow: hidden;
    box-shadow: 6px 7px 6px rgba(0, 0, 0, 0.28);
  }
  .card--front { top: 191px; background: var(--card-blue); }
  .card--back { top: 645px; background: var(--paper); color: var(--ink); }

  .card__band {
    position: absolute;
    left: 0;
    right: 0;
    bottom: 0;
    height: 112px;
    background: linear-gradient(180deg, var(--card-blue) 0%, var(--band-pale) 55%, var(--card-blue) 100%);
  }

  .card__mark {
    position: absolute;
    right: 48px;
    top: 232px;
    color: var(--mark-white);
    font-variant: small-caps;
    font-variant-numeric: lining-nums;
    font-size: 22px;
    font-weight: 400;
    letter-spacing: 0.5px;
  }

  .name {
    position: absolute;
    font-family: "Sacramento", cursive;
    font-size: 62px;
    line-height: 1;
    color: var(--ink);
    white-space: nowrap;
  }
  .name--first { left: 122px; top: 80px; }
  .name--last { left: 250px; top: 124px; }

  .credential {
    position: absolute;
    left: 391px;
    top: 190px;
    font-variant: small-caps;
    font-size: 20px;
    letter-spacing: 0.5px;
  }

  .contact {
    position: absolute;
    left: 0;
    right: 0;
    top: 261px;
    text-align: center;
    font-variant: small-caps;
    font-variant-numeric: lining-nums;
    line-height: 20px;
  }
  .contact__phone { font-size: 18px; font-weight: 500; font-variant: normal; font-variant-numeric: lining-nums; margin-bottom: 4px; letter-spacing: 0.6px; }
  .contact__line { font-size: 16px; letter-spacing: 0.2px; }
  .contact__email { font-size: 14px; letter-spacing: 0.3px; }
</style>
</head>
<body>

  <section class="card card--front" aria-label="Card front">
    <div class="card__band" role="img" aria-label="Soft flowing light band decoration along the lower edge"></div>
    <div class="card__mark">Lorna Pettigrew</div>
  </section>

  <section class="card card--back" aria-label="Card back">
    <div class="name name--first">lorna</div>
    <div class="name name--last">pettigrew</div>
    <div class="credential">Ph.D.</div>
    <div class="contact">
      <p class="contact__phone">312-555-0173</p>
      <p class="contact__line">462 W. Brambleton, Suite 2150</p>
      <p class="contact__line">Chicago, Illinois 60688</p>
      <p class="contact__email">drlornampettigrew@quenmail.example</p>
    </div>
  </section>

</body>
</html>
```